Business Card Design

We need a business card designed to portray the message that we are wedding and event stylists. We set up garden ceremonies and style wedding reception venues with chair covers and sashes, backdrops and draping's, wishing wells, tealight holders, table centerpieces. We also style corporate functions - Christmas parties, gala dinners, school formals, award nights. The colour of our uniforms are black and hot pink, if these colours could be incorporated. We would like to be able to use this design for letterhead, flyers and postcards etc. We would like the design to portray a professional, classic image that would relate to both spectrums of our business, weddings and corporate events. If you could develop a logo to incorporate would be great

Target Market(s)

brides, corporate compaines

Industry/Entity Type

Wedding

Contact Information for Business Card

Velvet Aisle & Function Rentals
Phone: 0413 586 190 Email:vaafr@quokkamail.com
Web: www.velvetaisleandfunctions.com.au

Requirements
Must have
• Must include that we set up for weddings, engagements, birthdays, anniversaries, corporate functions, school formals, any occasion.

```html
<!DOCTYPE html>
<html lang="en">
<head>
<meta charset="utf-8">
<title>Velvet Aisle &amp; Function Rentals – Business Card</title>
<link href="https://fonts.googleapis.com/css2?family=Great+Vibes&family=Raleway:wght@200;300&display=swap" rel="stylesheet">
<style>
  :root {
    --paper: #ffffff;
    --ink: #111111;
    --ink-soft: #3a3a3a;
    --leaf-light: #f3f7ec;
    --leaf-mid: #e6efd9;
  }
  html, body {
    margin: 0;
    padding: 0;
    overflow: hidden;
    background: var(--paper);
  }
  .card {
    position: relative;
    width: 1200px;
    height: 1105px;
    background: var(--paper);
    overflow: hidden;
  }
  .flourish {
    position: absolute;
    top: 186px;
    height: 728px;
  }
  .flourish--left {
    left: 0;
    width: 412px;
    background: radial-gradient(ellipse at 40% 50%, var(--leaf-mid) 0%, var(--leaf-light) 55%, rgba(255,255,255,0) 85%);
  }
  .flourish--right {
    left: 780px;
    width: 400px;
    background: radial-gradient(ellipse at 60% 50%, var(--leaf-mid) 0%, var(--leaf-light) 55%, rgba(255,255,255,0) 85%);
  }
  .brand-name {
    position: absolute;
    left: 0;
    width: 1200px;
    top: 400px;
    margin: 0;
    padding-left: 18px;
    box-sizing: border-box;
    text-align: center;
    font-family: "Great Vibes", cursive;
    font-weight: 400;
    font-size: 88px;
    line-height: 1;
    color: var(--ink);
    white-space: nowrap;
  }
  .brand-rule {
    position: absolute;
    left: 0;
    top: 0;
  }
  .services {
    position: absolute;
    left: 0;
    width: 1200px;
    margin: 0;
    text-align: center;
    font-family: "Raleway", sans-serif;
    font-weight: 300;
    font-variant: small-caps;
    font-size: 44px;
    line-height: 1;
    letter-spacing: -0.5px;
    color: var(--ink-soft);
    white-space: nowrap;
  }
  .services--primary { top: 530px; }
  .services--secondary { top: 584px; padding-left: 110px; box-sizing: border-box; }
  .services .sep { margin: 0 8px; font-weight: 200; }
  .contact {
    position: absolute;
    left: 0;
    width: 1200px;
    top: 656px;
    margin: 0;
    padding-right: 40px;
    box-sizing: border-box;
    text-align: center;
    font-family: "Raleway", sans-serif;
    font-weight: 300;
    font-size: 44px;
    line-height: 1;
    color: var(--ink-soft);
    white-space: nowrap;
  }
  .contact .person { font-variant: small-caps; margin-right: 22px; }
</style>
</head>
<body>
  <div class="card">
    <div class="flourish flourish--left" role="img" aria-label="Soft pale green swirling vine flourish"></div>
    <div class="flourish flourish--right" role="img" aria-label="Soft pale green swirling vine flourish"></div>

    <h1 class="brand-name">Velvet Aisle &amp; Function Rentals</h1>
    <svg class="brand-rule" width="1200" height="1105" viewBox="0 0 1200 1105" aria-hidden="true">
      <path d="M72 513 L880 511 Q920 510 940 498" fill="none" stroke="#111111" stroke-width="1.3"/>
    </svg>

    <p class="services services--primary">Weddings<span class="sep">|</span>Engagements<span class="sep">|</span>Anniversaries<span class="sep">|</span>Birthdays</p>
    <p class="services services--secondary">School<span class="sep">|</span>Formals<span class="sep">|</span>Corporate<span class="sep">|</span>Functions</p>

    <p class="contact">- <span class="person">Rosalind</span>0413 586 190 -</p>
  </div>
</body>
</html>
```